Redesign website for small print company

Vindaborgprent is a small printing company in Iceland mainly servicing Students, schools, etc. We are also doing all kind of other jobs, like business cards, book printing, brochure printing etc. We are also selling books online.
Our website is: www.vindaborgprent.is
What we are looking for is:
- Web Design (Uncoded - PSD layout only)
- Mobile friendly design, using our current color scheme: Red, green, yellow and light gray.
- Clean simple design
- Simple, light and easy to use.
- More menu Items/drop down
Industry/Entity Type
Digital Printing
Number of Pages Required
5+ page
Requirements
Must have
- Easy navigation
- Designed for mobile
- Current color scheme (see logo)
Nice to have
- Icon based products

```html
<!DOCTYPE html>
<html lang="en">
<head>
<meta charset="utf-8">
<title>Vindaborgprent</title>
<link rel="stylesheet" href="https://fonts.googleapis.com/css2?family=Montserrat:wght@500;600;700&family=Lato:ital,wght@0,400;0,700;1,400;1,700&family=Catamaran:wght@500&display=swap">
<style>
:root{
  --red:#ee3b3b;
  --green:#0f6b37;
  --green-light:#3f9140;
  --yellow:#ffd400;
  --gold:#f2c318;
  --ink:#2b2b2b;
  --muted:#6d6d6d;
  --panel:#f4f4f4;
  --line:#dedede;
  --white:#ffffff;
}
*{margin:0;padding:0;box-sizing:border-box}
html,body{width:1200px;height:2782px;overflow:hidden;background:var(--white)}
body{position:relative;font-family:"Lato",sans-serif;color:var(--ink)}
.abs{position:absolute}

/* header */
.site-header{position:absolute;left:0;top:0;width:1200px;height:117px;background:var(--white)}
.brand{position:absolute;left:78px;top:30px;display:flex;align-items:center;gap:14px}
.brand-square{width:54px;height:54px;background:var(--red)}
.brand-name{font-family:"Montserrat",sans-serif;font-weight:700;font-size:34px;color:#1d1d1d}
.nav{position:absolute;top:44px;left:0;width:1200px;font-size:17px;color:#8a8a8a}
.nav span{position:absolute;white-space:nowrap}
.nav .active{color:var(--red)}
.cart{font-family:"Montserrat",sans-serif;font-size:15px;color:#333}
.badge{position:absolute;left:1102px;top:40px;width:16px;height:16px;border-radius:50%;background:var(--yellow);font-size:10px;text-align:center;line-height:16px;font-weight:700}

/* hero */
.hero{position:absolute;left:0;top:117px;width:1200px;height:571px;background:linear-gradient(120deg,#3b3a38 0%,#6e6a64 45%,#45423e 100%)}
.hero-photo{position:absolute;inset:0;background:radial-gradient(ellipse at 55% 50%,rgba(180,150,120,.35),rgba(0,0,0,.25) 70%)}
.hero-title{position:absolute;top:160px;width:1200px;text-align:center;font-family:"Montserrat",sans-serif;font-weight:700;font-size:56px;color:var(--yellow)}
.hero-text{position:absolute;left:270px;top:245px;width:660px;text-align:center;font-style:italic;font-weight:700;font-size:14.5px;line-height:25px;color:var(--white)}
.btn{display:block;position:absolute;background:var(--red);color:var(--white);font-family:"Montserrat",sans-serif;font-size:18px;text-align:center}
.hero .btn{left:528px;top:345px;width:146px;height:48px;line-height:48px}
.dots{position:absolute;top:486px;left:572px;display:flex;gap:8px}
.dots i{width:12px;height:12px;border-radius:50%;border:1.5px solid var(--white)}
.dots i.on{background:var(--white)}

/* about */
.about{position:absolute;left:0;top:688px;width:1200px;height:440px;background:var(--green);overflow:hidden}
.about-curve{position:absolute;left:-300px;top:272px;width:1800px;height:600px;border-radius:50%;background:var(--white)}
.section-title{position:absolute;width:1200px;left:0;text-align:center;font-family:"Montserrat",sans-serif;font-weight:600;font-size:34px}
.about .section-title{top:48px;color:var(--white)}
.title-rule{position:absolute;height:2px}
.about-text{position:absolute;left:270px;top:112px;width:660px;text-align:center;font-size:14.5px;line-height:25px;color:var(--white)}
.feature{position:absolute;top:212px;width:200px;text-align:center}
.feature-icon{width:116px;height:116px;margin:0 auto;border-radius:50%;border:6px solid var(--white);box-shadow:0 3px 8px rgba(0,0,0,.25);display:flex;align-items:center;justify-content:center}
.feature-label{margin-top:24px;font-family:"Montserrat",sans-serif;font-weight:500;font-size:19px}

/* services */
.services .section-title{top:1120px;color:var(--ink)}
.card{position:absolute;width:332px;height:373px;background:var(--panel);border:1px solid #e7e7e7}
.card-photo{position:absolute;left:0;top:0;width:330px;height:188px}
.card-icon{position:absolute;left:121px;top:142px;width:88px;height:88px;border-radius:50%;background:var(--yellow);border:5px solid var(--white);box-shadow:0 2px 6px rgba(0,0,0,.3);display:flex;align-items:center;justify-content:center}
.card-title{position:absolute;top:250px;width:330px;text-align:center;font-family:"Catamaran",sans-serif;font-weight:500;font-size:27px;color:var(--green)}
.card-text{position:absolute;top:292px;left:25px;width:280px;text-align:center;font-size:14px;line-height:26px;color:var(--muted)}

/* signup */
.signup{position:absolute;left:0;top:2010px;width:1200px;height:375px;background:var(--green-light);overflow:hidden}
.signup-curve{position:absolute;left:-200px;top:-360px;width:1600px;height:470px;border-radius:50%;background:var(--white)}
.bubble{position:absolute;border-radius:50%;background:rgba(20,110,90,.45)}
.signup-title{position:absolute;left:78px;top:152px;font-family:"Montserrat",sans-serif;font-weight:600;font-size:34px;color:var(--white)}
.signup-text{position:absolute;left:78px;top:208px;width:620px;font-size:14.5px;line-height:27px;color:var(--white)}
.signup .btn{left:78px;top:282px;width:145px;height:51px;line-height:51px}
.signup-photo{position:absolute;left:790px;top:12px;width:332px;height:363px;border-radius:140px 140px 0 0;background:linear-gradient(180deg,#d9b79a 0%,#c23a3a 45%,#d9a23c 75%,#3c4f6e 100%)}

/* footer */
.footer{position:absolute;left:0;top:2385px;width:1200px;height:334px;background:var(--panel)}
.f-head{position:absolute;top:66px;font-family:"Montserrat",sans-serif;font-weight:600;font-size:17px;color:#222}
.f-links{position:absolute;left:78px;top:112px;font-size:14.5px;line-height:29px;color:#555}
.f-links .active{color:var(--green);font-weight:700}
.f-divider{position:absolute;top:60px;width:1px;height:170px;background:var(--line)}
.contact{position:absolute;left:273px;font-size:14.5px;line-height:24px;color:#555;display:flex;gap:16px}
.map{position:absolute;left:523px;top:64px;width:256px;height:207px;border:4px solid var(--white);box-shadow:0 0 0 1px var(--line);background:linear-gradient(135deg,#e8e3d6,#d6dbe0)}
.social{position:absolute;left:814px;display:flex;align-items:center;gap:14px;font-size:14.5px;color:#555}
.social i{width:32px;height:32px;border-radius:50%;border:1px solid #ccc;background:var(--white)}
.social i.fill{background:var(--green);border-color:var(--green)}
.footer-brand{position:absolute;left:979px;top:64px;width:126px;height:166px;display:flex;flex-direction:column;align-items:center;justify-content:center;gap:14px}
.footer-brand .brand-square{width:60px;height:60px}
.footer-brand .brand-name{font-size:15px}
.copyright{position:absolute;left:0;top:2719px;width:1200px;height:63px;background:var(--red);color:var(--white);text-align:center;line-height:63px;font-size:14px}
</style>
</head>
<body>

<header class="site-header">
  <div class="brand"><div class="brand-square"></div><div class="brand-name">Vindaborgprent</div></div>
  <nav class="nav">
    <span class="active" style="left:552px">Home</span>
    <span style="left:633px">Services</span>
    <span style="left:731px">Job submit</span>
    <span style="left:848px">About us</span>
    <span style="left:943px;top:2px"><svg width="20" height="20" viewBox="0 0 20 20"><circle cx="8" cy="8" r="6" fill="none" stroke="#0f6b37" stroke-width="2"/><line x1="12.5" y1="12.5" x2="18" y2="18" stroke="#0f6b37" stroke-width="2"/></svg></span>
    <span class="cart" style="left:997px;top:1px">MY CART <svg width="20" height="18" viewBox="0 0 20 18"><path d="M1 2h3l2 9h10l2-7H5" fill="none" stroke="#0f6b37" stroke-width="2"/><circle cx="8" cy="15" r="1.6" fill="#0f6b37"/><circle cx="15" cy="15" r="1.6" fill="#0f6b37"/></svg></span>
  </nav>
  <span class="badge">1</span>
</header>

<section class="hero">
  <div class="hero-photo" role="img" aria-label="Photo of two people looking over colour swatches and print samples in a print shop"></div>
  <h1 class="hero-title">Vindaborgprent</h1>
  <p class="hero-text">Lorem Ipsum is simply dummy text of the printing and typesetting industry. Lorem Ipsum has been the industry's standard dummy text ever since the 1500s, when an unknown printer took a galley of type and scrambled it to make a type specimen book.</p>
  <a class="btn">CONTACT US</a>
  <div class="dots"><i></i><i class="on"></i><i></i></div>
</section>

<section class="about">
  <div class="about-curve"></div>
  <span class="title-rule" style="left:392px;top:69px;width:90px;background:#fff"></span>
  <h2 class="section-title">ABOUT US</h2>
  <span class="title-rule" style="left:722px;top:69px;width:86px;background:#fff"></span>
  <p class="about-text">Lorem Ipsum is simply dummy text of the printing and typesetting industry. Lorem Ipsum has been the industry's standard dummy text ever since the 1500s, when an unknown printer took a galley of type and scrambled it to make a type specimen book.</p>
  <div class="feature" style="left:213px">
    <div class="feature-icon" style="background:var(--yellow)"><svg width="50" height="40" viewBox="0 0 50 40"><rect x="17" y="2" width="16" height="8" rx="2" fill="none" stroke="#fff" stroke-width="3"/><rect x="2" y="9" width="46" height="29" rx="3" fill="#fff"/><line x1="2" y1="20" x2="48" y2="20" stroke="#ffd400" stroke-width="2"/></svg></div>
    <div class="feature-label" style="color:var(--gold)">SENDA VERK</div>
  </div>
  <div class="feature" style="left:505px">
    <div class="feature-icon" style="background:var(--green)"><svg width="44" height="40" viewBox="0 0 44 40"><path d="M22 2C10 2 2 10 2 20s8 18 18 18c3 0 4-2 3-4s0-5 3-5h6c6 0 10-4 10-10C42 9 33 2 22 2z" fill="#fff"/><circle cx="12" cy="18" r="3" fill="#0f6b37"/><circle cx="18" cy="10" r="3" fill="#0f6b37"/><circle cx="28" cy="10" r="3" fill="#0f6b37"/><circle cx="34" cy="18" r="3" fill="#0f6b37"/></svg></div>
    <div class="feature-label" style="color:var(--green)">HANNA VERK</div>
  </div>
  <div class="feature" style="left:796px">
    <div class="feature-icon" style="background:var(--red)"><span style="font-family:Montserrat,sans-serif;font-weight:700;font-size:54px;color:#fff">?</span></div>
    <div class="feature-label" style="color:var(--red)">FA TILBOD</div>
  </div>
</section>

<section class="services">
  <span class="title-rule abs" style="left:360px;top:1143px;width:78px;background:#ccc"></span>
  <h2 class="section-title">OUR SERVICES</h2>
  <span class="title-rule abs" style="left:764px;top:1143px;width:78px;background:#ccc"></span>

  <article class="card" style="left:78px;top:1198px">
    <div class="card-photo" role="img" aria-label="Photo of a yellow typewriter on a desk" style="background:linear-gradient(135deg,#4a3322,#c9a53a 60%,#3a2a1e)"></div>
    <div class="card-icon"><svg width="36" height="40" viewBox="0 0 36 40"><rect x="5" y="3" width="26" height="34" rx="2" fill="none" stroke="#111" stroke-width="3"/><line x1="11" y1="12" x2="25" y2="12" stroke="#111" stroke-width="2.5"/><line x1="11" y1="19" x2="25" y2="19" stroke="#111" stroke-width="2.5"/><line x1="11" y1="26" x2="20" y2="26" stroke="#111" stroke-width="2.5"/></svg></div>
    <h3 class="card-title">Essays</h3>
    <p class="card-text">Lorem Ipsum is simply dummy text of the printing and typesetting industry.</p>
  </article>
  <article class="card" style="left:434px;top:1198px">
    <div class="card-photo" role="img" aria-label="Photo of two people exchanging a business card" style="background:linear-gradient(90deg,#d8d4cf,#8a7868 55%,#3c2e28)"></div>
    <div class="card-icon"><svg width="40" height="32" viewBox="0 0 40 32"><rect x="8" y="2" width="30" height="18" rx="2" fill="#111"/><rect x="2" y="11" width="30" height="18" rx="2" fill="#111" stroke="#ffd400" stroke-width="2"/><line x1="7" y1="18" x2="22" y2="18" stroke="#ffd400" stroke-width="2"/><line x1="7" y1="23" x2="18" y2="23" stroke="#ffd400" stroke-width="2"/></svg></div>
    <h3 class="card-title">Business Cards</h3>
    <p class="card-text">Lorem Ipsum is simply dummy text of the printing and typesetting industry.</p>
  </article>
  <article class="card" style="left:790px;top:1198px">
    <div class="card-photo" role="img" aria-label="Photo of hands reviewing printed leaflets on a table" style="background:linear-gradient(135deg,#b0856a,#e9e6e2 50%,#2f3340)"></div>
    <div class="card-icon"><svg width="38" height="36" viewBox="0 0 38 36"><path d="M3 6l10-3v27l-10 3z M15 3l10 3v27l-10-3z M27 6l8-3v27l-8 3z" fill="#111"/></svg></div>
    <h3 class="card-title">Lealfeats</h3>
    <p class="card-text">Lorem Ipsum is simply dummy text of the printing and typesetting industry.</p>
  </article>

  <article class="card" style="left:78px;top:1597px">
    <div class="card-photo" role="img" aria-label="Photo of colour print sheets coming out of a press" style="background:linear-gradient(160deg,#9a9a9a,#e6e6e6 55%,#c8c8c8)"></div>
    <div class="card-icon"><svg width="40" height="36" viewBox="0 0 40 36"><rect x="10" y="2" width="20" height="9" fill="#111"/><rect x="2" y="11" width="36" height="15" rx="3" fill="#111"/><rect x="10" y="22" width="20" height="12" fill="#111" stroke="#ffd400" stroke-width="2"/></svg></div>
    <h3 class="card-title">Book Printing</h3>
    <p class="card-text">Lorem Ipsum is simply dummy text of the printing and typesetting industry.</p>
  </article>
  <article class="card" style="left:434px;top:1597px">
    <div class="card-photo" role="img" aria-label="Photo of framed film posters on a dark wall" style="background:linear-gradient(90deg,#1f2a33,#4b5560 50%,#1e252c)"></div>
    <div class="card-icon"><svg width="34" height="38" viewBox="0 0 34 38"><rect x="5" y="2" width="24" height="22" fill="#111"/><line x1="9" y1="24" x2="4" y2="37" stroke="#111" stroke-width="3"/><line x1="25" y1="24" x2="30" y2="37" stroke="#111" stroke-width="3"/><line x1="7" y1="31" x2="27" y2="31" stroke="#111" stroke-width="2.5"/></svg></div>
    <h3 class="card-title">Posters</h3>
    <p class="card-text">Lorem Ipsum is simply dummy text of the printing and typesetting industry.</p>
  </article>
  <article class="card" style="left:790px;top:1597px">
    <div class="card-photo" role="img" aria-label="Photo of students studying together in a classroom" style="background:linear-gradient(135deg,#3b5566,#b78d74 55%,#2d3a52)"></div>
    <div class="card-icon"><svg width="30" height="40" viewBox="0 0 30 40"><rect x="3" y="2" width="24" height="36" rx="3" fill="#111"/><rect x="7" y="7" width="16" height="22" fill="#ffd400"/><line x1="10" y1="13" x2="20" y2="13" stroke="#111" stroke-width="2"/><line x1="10" y1="18" x2="20" y2="18" stroke="#111" stroke-width="2"/><circle cx="15" cy="33" r="2" fill="#ffd400"/></svg></div>
    <h3 class="card-title">Textbooks</h3>
    <p class="card-text">Lorem Ipsum is simply dummy text of the printing and typesetting industry.</p>
  </article>
</section>

<section class="signup">
  <div class="signup-curve"></div>
  <span class="bubble" style="left:12px;top:75px;width:52px;height:52px;opacity:.5"></span>
  <span class="bubble" style="left:512px;top:130px;width:136px;height:136px;opacity:.8"></span>
  <span class="bubble" style="left:380px;top:250px;width:40px;height:40px;opacity:.4"></span>
  <span class="bubble" style="left:1040px;top:250px;width:126px;height:126px;opacity:.9"></span>
  <span class="bubble" style="left:1100px;top:70px;width:40px;height:40px;opacity:.5"></span>
  <h2 class="signup-title">READY TO SIGN UP?</h2>
  <p class="signup-text">Lorem Ipsum is simply dummy text of the printing and typesetting industry. Lorem Ipsum has been the industry's standard dummy text ever since the 1500s.</p>
  <a class="btn">JOIN NOW</a>
  <div class="signup-photo" role="img" aria-label="Photo of a smiling student carrying a tall stack of books"></div>
</section>

<footer class="footer">
  <h4 class="f-head" style="left:78px">QUICK LINKS</h4>
  <div class="f-links"><div class="active">Home</div><div>About</div><div>Job Submit</div><div>About Us</div></div>
  <span class="f-divider" style="left:228px"></span>

  <h4 class="f-head" style="left:273px">GET IN TOUCH</h4>
  <div class="contact" style="top:112px"><svg width="18" height="22" viewBox="0 0 18 22"><path d="M9 1a7 7 0 0 0-7 7c0 5 7 12 7 12s7-7 7-12a7 7 0 0 0-7-7z" fill="none" stroke="#0f6b37" stroke-width="2.2"/><circle cx="9" cy="8" r="2.5" fill="#0f6b37"/></svg><div>48 Vindgata, Landmark,<br>Vindaborg 101</div></div>
  <div class="contact" style="top:180px"><svg width="20" height="20" viewBox="0 0 20 20"><path d="M4 1l4 4-2 3c1 3 3 5 6 6l3-2 4 4-3 3C8 19 1 12 1 4z" fill="#0f6b37"/></svg><div>+354 555 0142</div></div>
  <div class="contact" style="top:222px"><svg width="20" height="16" viewBox="0 0 20 16"><rect x="1" y="1" width="18" height="14" fill="#0f6b37"/><path d="M1 1l9 8 9-8" fill="none" stroke="#fff" stroke-width="1.6"/></svg><div>info@vindaborgprent.is</div></div>
  <span class="f-divider" style="left:490px"></span>

  <div class="map" role="img" aria-label="Street map showing the shop location"><svg width="248" height="199" viewBox="0 0 248 199" style="display:block"><path d="M124 70c-9 0-15 7-15 15 0 12 15 27 15 27s15-15 15-27c0-8-6-15-15-15z" fill="#ee3b3b"/><circle cx="124" cy="85" r="5" fill="#fff"/></svg></div>
  <span class="f-divider" style="left:772px"></span>

  <h4 class="f-head" style="left:814px">GET SOCIAL</h4>
  <div class="social" style="top:112px"><i class="fill"></i>Pagebook</div>
  <div class="social" style="top:164px"><i></i>Linkhub</div>
  <div class="social" style="top:216px"><i></i>Chirper</div>
  <span class="f-divider" style="left:958px"></span>

  <div class="footer-brand"><div class="brand-square"></div><div class="brand-name">Vindaborgprent</div></div>
</footer>

<div class="copyright">Copyright © <b>Vindaborgprent</b> - 2018 . All Right Reserved</div>

</body>
</html>
```